Web design for a Crane & Heavy Equipment Inspection, Repair and Maintenance Company in Texas

We need a web design for a new company based in Houston, Texas called "Bristen Hoist & Equipment". We inspect, repair and maintain diesel driven heavy equipment, generators, fire water pumps and cranes. We would like to see designs that use the colors orange, white, yellow and brown, and/or orange, white, navy, yellow and grey.

```html
<!DOCTYPE html>
<html lang="en">
<head>
<meta charset="utf-8">
<title>Bristen Hoist &amp; Equipment</title>
<link rel="stylesheet" href="https://fonts.googleapis.com/css2?family=Open+Sans:wght@400;600;700&family=PT+Sans+Narrow:wght@700&family=Raleway:wght@400;700&family=Roboto+Condensed:wght@400;700&display=swap">
<style>
:root{
  --navy:#054173;
  --navy-dark:#03365f;
  --orange:#fbab2c;
  --brand-orange:#ee5a24;
  --page:#eeeeee;
  --white:#ffffff;
  --ink:#222222;
  --muted:#777777;
  --line:#c9c9c9;
  --tick:#f7b520;
}
*{box-sizing:border-box;margin:0;padding:0}
html,body{width:941px;height:1200px;overflow:hidden}
body{position:relative;background:var(--page);font-family:"Open Sans",sans-serif;color:var(--ink)}
.abs{position:absolute}

.topbar{left:63px;top:0;width:815px;height:30px;display:flex;align-items:center;justify-content:space-between;font:400 11px "Roboto Condensed",sans-serif;color:#333}
.topbar .contact{display:flex;gap:18px;align-items:center}
.topbar .contact span{display:flex;align-items:center;gap:6px}
.social-top{display:flex;gap:14px}
.social-top i{display:block;width:9px;height:9px;border-radius:50%;background:#333}

.header{left:63px;top:30px;width:815px;height:97px;background:var(--white);box-shadow:0 0 3px rgba(0,0,0,.15)}
.brand{position:absolute;left:32px;top:34px;display:flex;align-items:center;gap:8px;font:700 22px "Open Sans",sans-serif;color:var(--navy);letter-spacing:-.3px}
.brand .dot{width:14px;height:14px;background:var(--brand-orange)}
.questions{position:absolute;right:14px;top:26px;text-align:right;font-family:"Roboto Condensed",sans-serif;color:#333}
.questions .q{font-size:18px}
.questions .tel{font-size:12px;margin-top:6px;display:flex;gap:6px;justify-content:flex-end;align-items:center}

.nav{left:63px;top:127px;width:815px;height:36px;background:var(--navy);display:flex;align-items:center}
.nav .home{width:41px;height:36px;background:var(--navy-dark);display:flex;align-items:center;justify-content:center}
.nav ul{list-style:none;display:flex;gap:30px;margin-left:19px;font:400 10.5px "Roboto Condensed",sans-serif;color:var(--white);text-transform:uppercase}
.nav .search{margin-left:auto;margin-right:14px;width:187px;height:24px;background:var(--navy-dark);display:flex;align-items:center;justify-content:space-between;padding:0 8px;font:400 10px "Roboto Condensed",sans-serif;color:#4d7398}

.hero{left:63px;top:163px;width:815px;height:243px;background:linear-gradient(180deg,#d9a24a 0%,#e8b966 45%,#c98b33 75%,#6b4a1f 100%)}
.hero-copy{left:108px;top:225px}
.hero-copy h1{font:700 29px "PT Sans Narrow",sans-serif;color:#1c1c1c}
.hero-copy p{font:400 9px "Open Sans",sans-serif;color:#2a2a2a;width:220px;line-height:1.3;margin-top:2px}
.hero-btn{left:108px;top:307px;width:86px;height:31px;background:var(--white);font:400 10px "Roboto Condensed",sans-serif;display:flex;align-items:center;justify-content:center;color:#333}

.promo{left:63px;top:435px;width:815px;height:107px;background:var(--orange);color:var(--white)}
.promo h2{position:absolute;left:28px;top:28px;font:600 27px "Open Sans",sans-serif;letter-spacing:.2px}
.promo p{position:absolute;left:28px;top:60px;font:400 19px "Open Sans",sans-serif}
.promo .more{position:absolute;right:28px;top:39px;width:109px;height:30px;border:2px solid var(--white);font:700 13px "Open Sans",sans-serif;display:flex;align-items:center;justify-content:center}

.story-head{left:63px;top:572px;width:815px;text-align:center}
.story-head .rule{position:absolute;top:27px;height:1px;background:var(--line);width:225px}
.story-head h2{font:700 25px "Raleway",sans-serif;color:#111}
.story-head p{font:400 9.5px "Raleway",sans-serif;color:#999;margin-top:6px;letter-spacing:.4px}

.about{left:63px;top:643px;width:815px;height:279px;background:var(--white)}
.about .photo{position:absolute;left:38px;top:35px;width:273px;height:214px;background:#ddd;padding:8px}
.about .photo div{width:100%;height:100%;background:linear-gradient(160deg,#3f6f9a 0%,#8fb2cc 55%,#c9d6df 100%)}
.about .text{position:absolute;left:348px;top:29px;width:400px}
.about h3{font:700 22px "Open Sans",sans-serif;color:var(--orange)}
.about h4{font:400 20px "Open Sans",sans-serif;color:#333;margin-top:-2px}
.about .lead{font:400 8.5px/1.6 "Open Sans",sans-serif;color:var(--muted);margin-top:10px}
.about ul{list-style:none;margin-top:12px}
.about li{font:700 9px "Open Sans",sans-serif;color:#333;display:flex;align-items:center;gap:9px;height:26.5px}

.footer{left:0;top:955px;width:941px;height:189px;background:var(--navy);color:var(--white)}
.footer .brand-f{position:absolute;left:82px;top:20px;width:150px;display:flex;align-items:center;gap:7px;font:700 14px/1.15 "Open Sans",sans-serif}
.footer .brand-f .dot{flex:none;width:10px;height:10px;background:var(--white)}
.footer .addr{position:absolute;left:83px;top:72px;font:400 7.5px/1.65 "Open Sans",sans-serif}
.footer .socials{position:absolute;left:84px;top:125px;display:flex;gap:5px}
.footer .socials i{width:15px;height:15px;border-radius:50%;background:#8a8f96;display:block}
.footer h5{position:absolute;top:29px;font:400 13px "Open Sans",sans-serif}
.footer .hear{position:absolute;left:292px;top:55px;width:140px;font:400 7.5px/2.05 "Open Sans",sans-serif}
.footer .links{position:absolute;left:514px;top:53px;width:95px;list-style:none;font:400 7.5px "Open Sans",sans-serif}
.footer .links li{border-bottom:1px dashed #c9d4e0;padding:5px 2px 5px}
.footer .map{position:absolute;left:668px;top:57px;width:164px;height:89px;background:radial-gradient(ellipse at center,#dcdcdc 0%,#c9c9c9 60%,rgba(201,201,201,0) 72%)}

.copyright{left:0;top:1163px;width:941px;text-align:center;font:400 7.5px "Open Sans",sans-serif;color:#333}
</style>
</head>
<body>

<div class="topbar abs">
  <div class="contact">
    <span><svg width="8" height="10" viewBox="0 0 8 10"><path d="M4 0a3.5 3.5 0 0 0-3.5 3.5C.5 6 4 10 4 10s3.5-4 3.5-6.5A3.5 3.5 0 0 0 4 0zm0 5a1.4 1.4 0 1 1 0-2.8A1.4 1.4 0 0 1 4 5z" fill="#333"/></svg>218 Calder Road, Houston</span>
    <span><svg width="11" height="8" viewBox="0 0 11 8"><rect width="11" height="8" fill="#333"/><path d="M0 0l5.5 4.5L11 0" stroke="#fff" fill="none"/></svg>hello@bristenhoist.test</span>
  </div>
  <div class="social-top"><i></i><i></i><i></i><i></i><i></i></div>
</div>

<header class="header abs">
  <div class="brand"><span class="dot"></span>Bristen Hoist &amp; Equipment</div>
  <div class="questions">
    <div class="q">ANY QUESTIONS?</div>
    <div class="tel"><svg width="10" height="10" viewBox="0 0 10 10"><path d="M2 0l2 2.5-1.2 1.3a6 6 0 0 0 3.4 3.4L7.5 6 10 8 8.5 10C4 10 0 6 0 1.5z" fill="#f39c12"/></svg>+1 713 555 0142</div>
  </div>
</header>

<nav class="nav abs">
  <div class="home"><svg width="14" height="12" viewBox="0 0 14 12"><path d="M7 0l7 6h-2v6H8.5V8h-3v4H2V6H0z" fill="#fff"/></svg></div>
  <ul><li>Services</li><li>Customer Care</li><li>About Us</li><li>Clients</li><li>Sitemap</li><li>FAQ's</li><li>Contact Us</li></ul>
  <div class="search">Search...<svg width="9" height="9" viewBox="0 0 9 9"><circle cx="3.6" cy="3.6" r="2.8" stroke="#4d7398" stroke-width="1.3" fill="none"/><path d="M5.8 5.8L8.5 8.5" stroke="#4d7398" stroke-width="1.4"/></svg></div>
</nav>

<div class="hero abs" role="img" aria-label="Mobile crane lifting a wooden crate against a golden sunset sky over hills"></div>
<div class="hero-copy abs">
  <h1>We Inspect &amp; Repair</h1>
  <p>repair and maintain diesel driven heavy equipment, generators, fire water pumps and cranes.</p>
</div>
<div class="hero-btn abs">GET START</div>

<section class="promo abs">
  <h2>WE INSPECT, REPAIR AND MAINTAIN</h2>
  <p>DRIVEN HEAVY EQUIPMENT, GENERATORS AND CRANES.</p>
  <div class="more">READ MORE</div>
</section>

<div class="story-head abs">
  <span class="rule" style="left:0"></span><span class="rule" style="right:0"></span>
  <h2>A SHORT STORY ABOUT US</h2>
  <p>DAPIBUS EGET. ELEMENTUM VEL</p>
</div>

<section class="about abs">
  <div class="photo"><div role="img" aria-label="Tower cranes rising against a blue sky"></div></div>
  <div class="text">
    <h3>WELCOME TO</h3>
    <h4>BRISTEN HOIST &amp; EQUIPMENT</h4>
    <p class="lead">We inspect, repair and maintain diesel driven heavy equipment, generators, fire water pumps and cranes. We provide vehicle recovery services and management information services to customers, maximizing effective use of the assets.</p>
    <ul>
      <li><svg width="11" height="9" viewBox="0 0 11 9"><path d="M1 4.5l3 3L10 1" stroke="#f7b520" stroke-width="2.2" fill="none"/></svg>We inspect, repair and maintain diesel driven heavy equipment.</li>
      <li><svg width="11" height="9" viewBox="0 0 11 9"><path d="M1 4.5l3 3L10 1" stroke="#f7b520" stroke-width="2.2" fill="none"/></svg>Maintain diesel driven heavy equipment.</li>
      <li><svg width="11" height="9" viewBox="0 0 11 9"><path d="M1 4.5l3 3L10 1" stroke="#f7b520" stroke-width="2.2" fill="none"/></svg>Provide heavy equipment, generators, fire water pumps and cranes.</li>
      <li><svg width="11" height="9" viewBox="0 0 11 9"><path d="M1 4.5l3 3L10 1" stroke="#f7b520" stroke-width="2.2" fill="none"/></svg>We inspect, repair and maintain diesel driven heavy equipment.</li>
    </ul>
  </div>
</section>

<footer class="footer abs">
  <div class="brand-f"><span class="dot"></span><span>Bristen Hoist<br>&amp; Equipment</span></div>
  <div class="addr">Tel: (713) 555-0187<br>Ridgeline Ave #12, Houston,<br>TX 77002</div>
  <div class="socials"><i></i><i></i><i></i><i></i><i></i></div>
  <h5 style="left:290px">We Want to Hear From You</h5>
  <p class="hear">We invite and encourage you to learn more about our unique approach to service. To speak to a member of our office staff or to set up an appointment, call Bristen Hoist &amp; Equipment today.</p>
  <h5 style="left:514px">Tweets</h5>
  <ul class="links"><li>Privacy Policy</li><li>Sitemap</li><li>Terms of Use</li></ul>
  <h5 style="left:674px">We are Located in</h5>
  <div class="map" role="img" aria-label="Grey world map showing company locations"></div>
</footer>

<div class="copyright abs">Copyright © BRISTEN HOIST &amp; EQUIPMENT | All Rights Reserved</div>

</body>
</html>
```